Velorin Global's Primary Marketing Brochure (Gate Fold Format)

We are looking for a main brochure design to communicate our company's primary mission, the need, where we meet the needs, how we meet the needs, and how the reader can get involved. We would like to see the color palette be similar to the colors of our company logo (attached). We would like to see a brochure design similar to a "gate fold" offering 22"x8.5" fully opened and 5.5"x8.5" when closed. Front panel, inside panels, full spread panel, and back panel. Required Text for each panel and usable picture suggestions are attached along with the company logo. The design should clean, contemporary, and emotionally compelling.

Target Market(s)

40-65 years old male and female, religious-minded

Industry/Entity Type

It Company

Font styles to use
Sans Serif

Requirements
Must have
• include text from attached WORD document.
• Clean, contemporary design
• Color in color palette of agency logo attached

```html
<!DOCTYPE html>
<html lang="en">
<head>
<meta charset="utf-8">
<title>Velorin Global – Gate Fold Brochure</title>
<link href="https://fonts.googleapis.com/css2?family=Open+Sans:ital,wght@0,400;0,600;0,700;1,400&display=swap" rel="stylesheet">
<style>
:root{
  --page:#e9e7e2;
  --blue:#2d3c9c;
  --blue-deep:#1d2770;
  --black:#050505;
  --gold:#b99b5f;
  --gold-light:#d9c49a;
  --tan:#d3bf95;
  --tan-dark:#b7985a;
  --white:#ffffff;
  --ink:#3a2e1a;
}
*{box-sizing:border-box;margin:0;padding:0}
html,body{width:1200px;height:1200px;overflow:hidden}
body{background:var(--page);font-family:"Open Sans",sans-serif;position:relative}
.spread{position:absolute;left:42px;width:1116px;height:431px;overflow:hidden;box-shadow:0 2px 6px rgba(0,0,0,.25)}
.spread--outside{top:142px}
.spread--inside{top:682px}
.panel{position:absolute;top:0;height:100%}
.abs{position:absolute}
.decor{position:absolute;inset:0;pointer-events:none}

/* outside */
.panel--back{left:0;width:277px;background:linear-gradient(90deg,var(--blue) 0%,var(--blue) 55%,var(--black) 100%)}
.panel--spread{left:277px;width:564px;background:
  linear-gradient(180deg,rgba(0,0,0,0) 55%,var(--blue) 100%),
  linear-gradient(90deg,var(--black) 0%,#6b5a36 20%,var(--gold) 45%,var(--gold) 70%,#5a4a2b 88%,var(--black) 100%)}
.panel--stats{left:841px;width:275px;background:linear-gradient(90deg,var(--black) 0%,var(--blue-deep) 35%,var(--blue) 100%)}
.map{left:10px;top:58px;width:260px;height:132px;border-radius:6px;
  background:radial-gradient(ellipse at 50% 50%,rgba(200,160,90,.55),rgba(120,95,60,.25) 60%,transparent 80%)}
.countries{top:213px;font-size:9px;line-height:9.85px;color:var(--white)}
.countries--a{left:78px}.countries--b{left:160px}
.mission{left:40px;top:50px;width:200px;text-align:center;color:var(--white);font-size:10px;line-height:21.6px}
.brand{display:flex;align-items:center;gap:6px;color:var(--gold-light);font-weight:700;font-size:18px;letter-spacing:.2px}
.brand__dot{width:22px;height:22px;border-radius:50%;border:2px solid var(--gold-light)}
.brand--mid{left:62px;top:240px}
.brand--cover{left:345px;top:358px;font-size:20px}
.contact{left:50px;top:296px;list-style:none;color:var(--white);font-size:7.4px;line-height:11px}
.contact li{display:flex;align-items:center;gap:3px}
.contact svg{width:8px;height:8px}
.badge{left:117px;top:358px;width:36px;height:36px;border-radius:50%;background:#1f3b7a;border:3px solid #c9ccd6}
.cover-title{left:307px;top:14px;color:var(--white);font-size:24px;line-height:28px;font-weight:400}
.cover-since{left:307px;top:104px;color:var(--white);font-size:16px;font-style:italic}
.cover-photo{left:283px;top:134px;width:278px;height:180px;border-radius:30px 30px 60% 60%/30px 30px 30% 30%;
  background:radial-gradient(ellipse at 50% 45%,#a8673e 0%,#6e3e22 35%,#2c2116 70%,rgba(20,20,30,.2) 100%)}
.stat{left:0;width:275px;text-align:center;color:var(--white)}
.stat__num{font-weight:700;font-size:36px;line-height:40px}
.stat__num sup{font-size:18px;vertical-align:top;line-height:26px}
.stat__text{font-size:10px;line-height:12px;padding:0 18px}

/* inside */
.panel--who{left:0;width:277px;background:var(--tan)}
.panel--areas{left:277px;width:564px;background:var(--tan-dark)}
.panel--help{left:841px;width:275px;background:var(--tan)}
h2{position:absolute;color:var(--white);font-weight:700;font-size:16px;line-height:15px}
.body{position:absolute;color:var(--ink);font-size:6.6px;line-height:8.6px}
.body p+p{margin-top:4px}
.who-heading{left:26px;top:11px;width:200px}
.who-body{left:26px;top:49px;width:190px}
.who-tagline{left:26px;top:179px;width:170px;color:var(--white);font-weight:700;font-size:10px;line-height:11px}
.photo-man{left:0;top:278px;width:277px;height:153px;background:linear-gradient(90deg,#7f8a68 0%,#6b5a48 45%,#4a3527 75%,#6b5a48 100%)}
.areas-heading{left:22px;top:11px}
.areas-list{position:absolute;left:22px;top:36px;width:190px;list-style:none}
.areas-list li{margin-bottom:8.5px}
.areas-list b{display:block;color:var(--white);font-size:10.5px;line-height:13px}
.areas-list span{display:block;color:var(--ink);font-size:6.8px;line-height:9px}
.photo-road{left:217px;top:0;width:347px;height:278px;background:linear-gradient(180deg,#6f8a5a 0%,#a8876a 30%,#b0704e 65%,#a0654a 100%);
  -webkit-mask:linear-gradient(90deg,transparent 0,#000 18%);mask:linear-gradient(90deg,transparent 0,#000 18%)}
.photo-children{left:0;top:270px;width:564px;height:161px;background:linear-gradient(90deg,#8f7055 0%,#c4a184 30%,#a07c62 55%,#d4b39a 80%,#9b7a60 100%);
  -webkit-mask:linear-gradient(180deg,transparent 0,#000 14%);mask:linear-gradient(180deg,transparent 0,#000 14%)}
.help-heading{left:20px;top:11px}
.photo-studio{left:149px;top:0;width:126px;height:278px;background:linear-gradient(180deg,#d8d3cc 0%,#a8674e 45%,#7a3a38 75%,rgba(150,130,110,.6) 100%);
  -webkit-mask:linear-gradient(90deg,transparent 0,#000 25%);mask:linear-gradient(90deg,transparent 0,#000 25%)}
.help-item{position:absolute;left:20px}
.help-item__head{display:flex;align-items:center;gap:4px;color:var(--white);font-weight:700;font-size:10.5px;margin-bottom:3px}
.help-item__icon{width:20px;height:20px;border-radius:50%;border:1.5px solid var(--white);display:flex;align-items:center;justify-content:center}
.help-item__icon svg{width:11px;height:11px}
.help-item .body{position:static}
.help-cta{position:absolute;left:20px;top:408px;color:var(--white);font-weight:700;font-size:10.5px}
</style>
</head>
<body>

<section class="spread spread--outside">
  <div class="panel panel--back">
    <div class="abs map" role="img" aria-label="Dotted world map with white stars marking ministry countries"></div>
    <div class="abs countries countries--a">Albania<br>Argentina<br>Australia<br>Bulgaria<br>Bangladesh<br>Canada<br>Costa Rica<br>Cuba<br>Cyprus<br>Egypt<br>Greece<br>Guatemala<br>Ghana<br>Haiti<br>India<br>Indonesia<br>Italy</div>
    <div class="abs countries countries--b">Kenya<br>Lebanon<br>Liberia<br>Mexico<br>Moldova<br>Myanmar<br>Pakistan<br>Peru<br>Philippines<br>Romania<br>South Africa<br>Spain<br>Thailand<br>Turkey<br>Uganda<br>United States<br>Zimbabwe</div>
  </div>

  <div class="panel panel--spread">
    <p class="abs mission">Velorin Global exists<br>to encourage, equip, and develop<br>Christ-centered national leaders<br>to become instruments of<br>Gospel advancement and<br>community transformation,<br>and has since 1942.</p>
    <div class="abs brand brand--mid"><span class="brand__dot"></span>Velorin Global</div>
    <ul class="abs contact">
      <li><svg viewBox="0 0 10 10"><path d="M5 0.5a3.2 3.2 0 0 0-3.2 3.2C1.8 6.2 5 9.5 5 9.5s3.2-3.3 3.2-5.8A3.2 3.2 0 0 0 5 .5z" fill="#fff"/><circle cx="5" cy="3.7" r="1.2" fill="#6b5a36"/></svg>1420 Larkmoor Ave. Brenton, OH. 44190-2210</li>
      <li><svg viewBox="0 0 10 10"><circle cx="5" cy="5" r="4.5" fill="#fff"/></svg>www.veloringlobal.org</li>
      <li><svg viewBox="0 0 10 10"><path d="M2 1l2 .3.6 2-1.2.9a6 6 0 0 0 2.4 2.4l.9-1.2 2 .6.3 2c-4 .6-7.6-3-7-7z" fill="#fff"/></svg>800-555-0142</li>
      <li><svg viewBox="0 0 10 10"><circle cx="5" cy="5" r="4.5" fill="#fff"/></svg>social/VelorinGlobal</li>
      <li><svg viewBox="0 0 10 10"><circle cx="5" cy="5" r="4.5" fill="#fff"/></svg>social/VELORINGL</li>
    </ul>
    <div class="abs badge" role="img" aria-label="Accreditation badge"></div>

    <h1 class="abs cover-title">Transforming<br>Nations with<br>the Gospel</h1>
    <p class="abs cover-since">...since 1942</p>
    <div class="abs cover-photo" role="img" aria-label="Portrait of a woman wearing a patterned headscarf"></div>
    <div class="abs brand brand--cover"><span class="brand__dot"></span>Velorin Global</div>
  </div>

  <div class="panel panel--stats">
    <div class="abs stat" style="top:94px"><div class="stat__num">3.11</div><p class="stat__text">billion people around the world are unreached and need to hear the Gospel</p></div>
    <div class="abs stat" style="top:172px"><div class="stat__num">16000</div><p class="stat__text">About 16,000 children under the age of five die each day from preventable causes</p></div>
    <div class="abs stat" style="top:250px"><div class="stat__num">&gt;85<sup>%</sup></div><p class="stat__text">More than 85 percent of the pastors around the world have never received theological education or pastoral preparation</p></div>
  </div>

  <svg class="decor" viewBox="0 0 1116 431" aria-hidden="true">
    <path d="M525 134 Q760 200 838 6" fill="none" stroke="#fff" stroke-width="1.2" opacity=".8"/>
    <path d="M532 142 Q770 200 845 4" fill="none" stroke="#fff" stroke-width=".6" opacity=".6"/>
    <path d="M566 268 Q760 380 945 255" fill="none" stroke="#fff" stroke-width="1.2" opacity=".8"/>
    <path d="M590 280 Q800 370 960 262" fill="none" stroke="#fff" stroke-width=".6" opacity=".6"/>
  </svg>
</section>

<section class="spread spread--inside">
  <div class="panel panel--who">
    <h2 class="who-heading">Who is a National Worker?</h2>
    <div class="body who-body">
      <p>National workers are native missionaries who reach their own people with the Gospel. They are the hands and feet of Velorin in the countries where we minister.</p>
      <p>National workers are unique. Because they serve in their own countries, they don't need special government residence permits and they are already experts with the local language and culture. They can even serve in countries where cross-cultural missionaries would not be allowed and they serve at a fraction of the cost a foreign missionary would need to raise.</p>
    </div>
    <p class="abs who-tagline">At the heart of every Velorin Ministry is a National Worker</p>
    <div class="abs photo-man" role="img" aria-label="Close portrait of a national worker"></div>
  </div>

  <div class="panel panel--areas">
    <div class="abs photo-road" role="img" aria-label="Young boy carrying water containers on a red dirt road"></div>
    <div class="abs photo-children" role="img" aria-label="Close portraits of three young children"></div>
    <h2 class="areas-heading">5 Areas of Ministry</h2>
    <ul class="areas-list">
      <li><b>Child Sponsorship</b><span>Bringing children out of poverty and teaching them to serve in the local church.</span></li>
      <li><b>Disciple Makers</b><span>Training and resourcing pastors and church planters.</span></li>
      <li><b>Medical Care</b><span>Physically showing the love of Christ while sharing the spiritual healing of Jesus.</span></li>
      <li><b>Media Evangelism</b><span>Using newspapers and radio to share the love of Christ in hostile regions of the world.</span></li>
      <li><b>Disaster Relief</b><span>Sharing the love of Christ where disaster has struck by meeting physical needs.</span></li>
    </ul>
  </div>

  <div class="panel panel--help">
    <div class="abs photo-studio" role="img" aria-label="Smiling radio host with headphones at a studio microphone"></div>
    <h2 class="help-heading">How Can I Help?</h2>
    <div class="help-item" style="top:44px;width:120px">
      <div class="help-item__head"><span class="help-item__icon"><svg viewBox="0 0 12 12"><path d="M1 8h10M3 8V6l3-2 3 2v2" fill="none" stroke="#fff"/></svg></span>Giving</div>
      <p class="body">Financially supporting Velorin through monthly, quarterly, annual, or one-time gifts. This can be done through our sponsorship programs or general support of the overall mission of Velorin worldwide.</p>
    </div>
    <div class="help-item" style="top:126px;width:124px">
      <div class="help-item__head"><span class="help-item__icon"><svg viewBox="0 0 12 12"><circle cx="6" cy="2" r="1.3" fill="#fff"/><path d="M6 4v4l-2 3M6 8l2 3M3 6h6" stroke="#fff" fill="none"/></svg></span>Going</div>
      <p class="body">Serve alongside a Velorin national worker on one of Velorin's many short-term mission team opportunities throughout the year; serve as a mission intern locally or on the foreign field; or even pray about serving as one of Velorin's long-term missionaries.</p>
    </div>
    <div class="help-item" style="top:217px;width:118px">
      <div class="help-item__head"><span class="help-item__icon"><svg viewBox="0 0 12 12"><path d="M6 2v8M3 10l3-5 3 5" stroke="#fff" fill="none"/></svg></span>Praying</div>
      <p class="body">Join us in praying daily for the Lord's work happening through all of Velorin's ministries. Velorin's monthly newsletter, VELORIN NEWS, contains our daily prayer guide for suggestions on how to pray specifically for Velorin's work around the world</p>
    </div>
    <div class="help-item" style="top:307px;width:240px">
      <div class="help-item__head"><span class="help-item__icon"><svg viewBox="0 0 12 12"><path d="M2 5h2l5-3v8L4 7H2z" fill="none" stroke="#fff"/></svg></span>Publicizing</div>
      <div class="body">
        <p>Tell others about the great work you are supporting and connected to at Velorin. Let your church know about the opportunity to partner with an organization that is advancing the Gospel worldwide. Share using social media to let others know all that is happening through your generosity and partnership with Velorin.</p>
        <p>Your partnership in giving, going, praying, and publicizing the mission of Velorin is a key element that allows us to build upon our 75-year history of equipping national workers, empowering the local church, and transforming communities with the Gospel of Jesus Christ.</p>
      </div>
    </div>
    <p class="help-cta">Partner with Velorin Today!</p>
  </div>

  <svg class="decor" viewBox="0 0 1116 431" aria-hidden="true">
    <path d="M6 250 Q230 235 272 14" fill="none" stroke="#fff" stroke-width="1.2" opacity=".85"/>
    <path d="M14 244 Q222 222 262 20" fill="none" stroke="#fff" stroke-width=".6" opacity=".7"/>
    <path d="M1080 10 Q1010 200 1070 340" fill="none" stroke="#fff" stroke-width="1.2" opacity=".85"/>
    <path d="M1090 16 Q1022 200 1084 332" fill="none" stroke="#fff" stroke-width=".6" opacity=".7"/>
  </svg>
</section>

</body>
</html>
```